Letterhead for Dane Holloway

I need a letterhead based on the business card design

Industry/Entity Type

Business

Requirements
Must have
• Footer: Dane Holloway Naturopath
Shop 3042c, 451 Marrow Lane, Sydney 2000

```html
<!DOCTYPE html>
<html lang="en">
<head>
<meta charset="utf-8">
<title>Dane Holloway Naturopath – Letterhead</title>
<link href="https://fonts.googleapis.com/css2?family=Montserrat:wght@300;500&family=Oswald:wght@300;500&display=swap" rel="stylesheet">
<style>
  :root {
    --backdrop: #e6e6e6;
    --paper: #ffffff;
    --brand-orange: #ef8a2e;
    --footer-orange: #f2a25a;
    --leaf-peach: #f5c9a0;
    --leaf-pale: #fbe6d3;
    --ink: #5a5a5a;
    --ink-strong: #333333;
    --signature-blue: #dbe3f0;
  }
  * { margin: 0; padding: 0; box-sizing: border-box; }
  html, body {
    width: 942px; height: 1200px; overflow: hidden;
    background: var(--backdrop);
  }
  .letterhead {
    position: absolute; left: 44px; top: 0;
    width: 854px; height: 1200px;
    background: var(--paper);
    font-family: "Oswald", "Arial Narrow", sans-serif;
    font-weight: 300;
    color: var(--ink);
    overflow: hidden;
  }
  .leaf-decoration {
    position: absolute; left: 0; top: 640px; z-index: 0;
    width: 206px; height: 560px;
    background: linear-gradient(160deg, rgba(251,230,211,0) 0%, var(--leaf-pale) 35%, var(--leaf-peach) 100%);
    border-top-right-radius: 100% 60%;
  }
  .signature-area {
    position: absolute; left: 112px; top: 826px; z-index: 0;
    width: 232px; height: 118px;
    background: radial-gradient(ellipse at center, var(--signature-blue) 0%, rgba(219,227,240,0) 70%);
  }
  .brand-name, .meta, .letter-body, .sign-off, .footer { z-index: 1; }
  .brand-name {
    position: absolute; top: 62px; left: 0; width: 100%;
    text-align: center;
    font-family: "Montserrat", sans-serif;
    font-weight: 500; font-size: 29px; letter-spacing: 0.5px;
    color: var(--brand-orange);
  }
  .meta {
    position: absolute; left: 113px; top: 244px;
    font-size: 13.5px; line-height: 24px; color: var(--ink-strong);
  }
  .meta b { font-weight: 500; }
  .letter-body {
    position: absolute; left: 113px; top: 316px; width: 668px;
    font-size: 13.8px; line-height: 24.6px; text-align: justify;
  }
  .letter-body p { margin-bottom: 24px; }
  .letter-body .salutation { margin-bottom: 0; }
  .sign-off {
    position: absolute; left: 113px; top: 756px;
    font-size: 13.5px; line-height: 15px; color: var(--ink-strong);
  }
  .sign-off .signer { font-weight: 500; text-transform: uppercase; }
  .footer {
    position: absolute; left: 0; top: 1140px; width: 100%;
    font-family: "Montserrat", sans-serif; font-weight: 300;
    font-size: 10px; line-height: 17px; color: var(--footer-orange);
    white-space: nowrap;
  }
  .footer-col {
    position: absolute; top: 0;
    border-left: 1px solid var(--footer-orange);
    padding-left: 9px;
  }
  .footer-col.address { left: 206px; }
  .footer-col.contact { left: 451px; }
  .footer-col.web { left: 601px; }
</style>
</head>
<body>
  <main class="letterhead">
    <div class="leaf-decoration" role="img" aria-label="Decorative cluster of translucent peach leaves"></div>
    <div class="signature-area" role="img" aria-label="Handwritten signature"></div>

    <header class="brand-name">DANE HOLLOWAY</header>

    <section class="meta">
      <div><b>Data :</b> Mon , 25 / 3 / 2013</div>
      <div><b>Recipient :</b> Mr.John Doe Sanderson</div>
    </section>

    <section class="letter-body">
      <p class="salutation">Dear Mr. Jhon Doe</p>
      <p>LoTrem ipsum dolor sit amet, consectetur adipiscing elit. Praesent vulputate, neque ac accumsan suscipit, justo turpis volutpat nisl, tempus fermentum eros tortor et elit. Vivamus porttitor faucibus gravida. Quisque pharetra gravida luctus. Donec eget turpis libero. Ut ac dolor urna, quis tempor nunc. Donec vitae mauris purus, euismod eleifend nulla. Lorem ipsum dolor sit amet, consectetur adipiscing elit. Donec ut purus tellus. Aenean quis dignissim lacus. Vestibulum suscipit vehicula cursus. Suspendisse potenti. Ut in sem nisi. Sed et massa leo.</p>
      <p>Fusce varius libero vel risus condimentum suscipit. Nullam tristique ultrices massa a volutpat. Donec sed dictum metus. Curabitur fringilla nibh eu ligula pharetra a interdum quam aliquam. Maecenas aliquam elit eu orci rutrum molestie. Proin nisl justo, varius a volutpat nec, ultricies sed sem. Nam sit amet imperdiet sem. Phasellus vitae mauris odio. Etiam in purus dui. Etiam ultricies, ante vel iaculis sodales, arcu leo adipiscing leo, sit amet mollis dui nisi non quam.</p>
      <p>Suspendisse sagittis laoreet dolor, vitae rhoncus arcu volutpat quis. Vestibulum at placerat dolor. Vivamus eu lacus ut enim molestie consectetur. Quisque ac lorem vel orci sagittis sollicitudin. Nunc ut quam sem, quis volutpat libero. Cum sociis natoque penatibus et magnis dis parturient montes, nascetur ridiculus mus. Vestibulum ante ipsum primis in faucibus orci luctus et ultrices posuere cubilia Curae; Donec tempor velit in velit feugiat sit amet vulputate nisl posuere..</p>
    </section>

    <section class="sign-off">
      <div class="signer">John Doe</div>
      <div class="role">General director</div>
    </section>

    <footer class="footer">
      <div class="footer-col address">
        Dane Holloway Naturopath<br>
        Shop 3042c, 451 Marrow Lane, Sydney 2000
      </div>
      <div class="footer-col contact">
        0400 123 456<br>
        dhnaturopath@mail.com
      </div>
      <div class="footer-col web">
        daneholloway.com.au<br>
        verdantdrops.com.au
      </div>
    </footer>
  </main>
</body>
</html>
```